Swim School Certificates

We are looking to have some certificates designed for our Learn to Swim School. These will be handed out to our students when they complete each level. We will need different certificates for each level, however, we would like a consistent theme throughout, so each level may only have a slight variation. We are happy for you to just show us a couple of variations to begin with, so we can see how these would work. Then once we decide on the winning design, you can complete the rest.
The levels are:
Bubs 1
Bubs 2
Toddler 1
Toddler 2
Beginner 1
Beginner 2
Beginner 3
Stroke Development 1
Stroke Development 2
Advanced 1
Advanced 2
Squad
The Certificates should include:
Congratulations to:
(blank line for name)
You have completed (level name), Keep up the good work!!!
Signed: (blank line) Date: (blank line)
I've included a copy of our logo, and a copy of our governing bodies logo both of which should be included on the certificate.
I've also included some examples of certificates we like, to give you an idea of our style. We are happy for the bubs and toddler certificates to be more child focused, so they can included a kid friendly element to them, however this will need to reduce to a more simplistic design as the levels increase into beginner and stroke etc.
You can also look on our Facebook page to get an idea of what we do.
https://www.facebook.com/ripplecoveswimschool/?ref=bookmarks
We will also need editable source files upon completion as we may be looking to change the name of some classes in the future.
Please let us know if you need any of the files in other formats
Kind Regards
Maree

```html
<!DOCTYPE html>
<html lang="en">
<head>
<meta charset="utf-8">
<title>Ripple Cove Swim School – Beginner 1 Certificate</title>
<link rel="stylesheet" href="https://fonts.googleapis.com/css2?family=Almendra:wght@700&family=Montserrat:wght@400;500;600&display=swap">
<style>
  :root {
    --backdrop: #4a4a4a;
    --navy: #0d4f95;
    --royal: #0a6fbf;
    --deep: #0560a0;
    --cyan: #00b4ec;
    --ink: #111111;
    --text-blue: #1566b0;
    --paper: #ffffff;
    --mist: #d9ecf8;
  }
  * { box-sizing: border-box; margin: 0; padding: 0; }
  html, body {
    width: 1200px; height: 1200px; overflow: hidden;
    background: var(--backdrop);
  }
  .certificate {
    position: absolute; left: 140px; top: 272px;
    width: 920px; height: 656px;
    overflow: hidden;
    font-family: "Montserrat", sans-serif;
  }
  .certificate__art { position: absolute; inset: 0; width: 100%; height: 100%; }
  .heading {
    position: absolute; left: 0; width: 100%; top: 150px;
    text-align: center;
    font-family: "Almendra", serif; font-weight: 700;
    font-size: 78px; color: var(--navy); line-height: 1;
  }
  .recipient {
    position: absolute; left: 188px; top: 273px;
    display: flex; align-items: baseline; gap: 12px;
    font-size: 23px; font-weight: 500; color: var(--ink);
  }
  .recipient__line {
    display: inline-block; width: 505px;
    border-bottom: 2px dotted #333; transform: translateY(-2px);
  }
  .achievement {
    position: absolute; left: 0; width: 100%; top: 328px;
    text-align: center; font-size: 23px; font-weight: 500;
    color: var(--text-blue); letter-spacing: 0.3px; word-spacing: 2px;
  }
  .sign-field { position: absolute; top: 408px; text-align: center; }
  .sign-field__line { border-top: 1px dotted #444; }
  .sign-field__label { margin-top: 12px; font-size: 14px; color: var(--ink); }
  .sign-field--signature { left: 41px; width: 265px; }
  .sign-field--signature .sign-field__label { padding-left: 0; }
  .sign-field--date { left: 708px; width: 166px; }
  .partner-badge {
    position: absolute; left: 40px; top: 538px;
    width: 84px; height: 84px; border-radius: 50%;
    border: 4px solid var(--paper); background: var(--royal);
  }
  .school-mark {
    position: absolute; left: 772px; top: 550px;
    width: 114px; height: 76px;
    display: flex; align-items: center; justify-content: center; gap: 6px;
    font-size: 15px; font-weight: 600; color: var(--paper);
    line-height: 1.15; text-align: left;
  }
  .school-mark__square {
    width: 12px; height: 12px; background: var(--paper); flex: none;
  }
</style>
</head>
<body>
  <main class="certificate">
    <svg class="certificate__art" viewBox="0 0 1151 820" preserveAspectRatio="none" aria-hidden="false">
      <defs>
        <radialGradient id="paperGlow" cx="0.5" cy="0.42" r="0.7">
          <stop offset="0" stop-color="#ffffff"/>
          <stop offset="0.6" stop-color="#eef6fc"/>
          <stop offset="1" stop-color="#d2e8f7"/>
        </radialGradient>
        <linearGradient id="waterFill" x1="0" y1="0" x2="0" y2="1">
          <stop offset="0" stop-color="#cfe6f7"/>
          <stop offset="0.25" stop-color="#5aa6e0"/>
          <stop offset="0.55" stop-color="#1164bf"/>
          <stop offset="1" stop-color="#0a6cbc"/>
        </linearGradient>
      </defs>
      <rect class="paper" width="1151" height="820" fill="url(#paperGlow)"/>
      <polygon class="corner corner--left" points="0,0 435,37 0,210" fill="var(--royal)"/>
      <polygon class="corner corner--left-top" points="0,0 330,0 435,37" fill="var(--royal)"/>
      <polygon class="band band--cyan" points="315,0 630,0 1151,245 1151,248 435,37" fill="var(--cyan)"/>
      <polygon class="corner corner--right" points="630,0 1151,0 1151,245" fill="var(--deep)"/>
      <path class="water" role="img" aria-label="Blue water wave with splashing droplets"
        d="M0,565 C120,620 260,650 420,600 C520,570 620,640 760,660 C880,670 930,560 1151,550 L1151,820 L0,820 Z"
        fill="url(#waterFill)"/>
    </svg>

    <h1 class="heading">Congratulations !</h1>

    <p class="recipient"><span>TO :</span><span class="recipient__line"></span></p>

    <p class="achievement">You have completed&nbsp; Beginner 1 , Keep up the good work!!</p>

    <div class="sign-field sign-field--signature">
      <div class="sign-field__line"></div>
      <p class="sign-field__label">Signature</p>
    </div>
    <div class="sign-field sign-field--date">
      <div class="sign-field__line"></div>
      <p class="sign-field__label">Date</p>
    </div>

    <div class="partner-badge" role="img" aria-label="Governing body registration badge"></div>

    <div class="school-mark">
      <span class="school-mark__square"></span>
      <span>Ripple Cove<br>Swim School</span>
    </div>
  </main>
</body>
</html>
```